Bread Baking Blog

I need theme modification/customization and logo for a Wordpress theme that I can use the blog about bread baking. Needs to include pictures & recipes.

Can provide access to my pagelumen.com site. Have paid for https://quilvanstore.com/themes/brisk/ but open to alternatives.

The site name is "velmo42.com" (type 85 flour is a type of bread flour used in artisan bread baking). Not particular on color palette - am looking for your creativity.

I've included some logos for other domains I have to help provide some inspiration.

```html
<!DOCTYPE html>
<html lang="en">
<head>
<meta charset="utf-8">
<title>Velmo42.com — Bread Baking Blog</title>
<link href="https://fonts.googleapis.com/css2?family=Mulish:wght@400;600;700;800;900&display=swap" rel="stylesheet">
<style>
:root{
  --orange:#f2891c;
  --orange-dark:#e07810;
  --ink:#222222;
  --text:#555555;
  --muted:#8a8a8a;
  --panel:#f2f2f2;
  --line:#e3e3e3;
  --footer:#2e2c2b;
  --footer-deep:#232120;
  --white:#ffffff;
}
*{box-sizing:border-box;margin:0;padding:0}
html,body{width:1200px;height:3608px;overflow:hidden}
body{font-family:"Mulish",Arial,sans-serif;color:var(--text);background:var(--white);position:relative}
.btn{display:inline-block;background:var(--orange);color:var(--white);font-weight:800;font-size:12px;letter-spacing:.5px;text-transform:uppercase;border-radius:20px;padding:9px 20px}
.btn-sm{font-size:10px;padding:6px 13px}

/* header + hero */
.hero{position:absolute;left:0;top:0;width:1200px;height:592px;overflow:hidden}
.hero-photo{position:absolute;inset:0;background:linear-gradient(100deg,#2a1d14 0%,#3d2a1c 35%,#6b4a30 60%,#8a6a4c 80%,#4a3323 100%)}
.hero-shade{position:absolute;inset:0;background:linear-gradient(90deg,rgba(0,0,0,.55) 0%,rgba(0,0,0,.2) 55%,rgba(0,0,0,0) 100%)}
.site-header{position:absolute;left:0;top:0;width:1200px;height:88px;display:flex;align-items:center;padding:0 152px 0 160px;background:rgba(20,14,10,.35)}
.brand{font-weight:900;font-size:30px;color:var(--orange);letter-spacing:-.5px;line-height:1}
.main-nav{display:flex;gap:28px;margin-left:auto;align-items:center}
.main-nav a{color:var(--white);font-size:13px;font-weight:600;text-decoration:none}
.search-icon{margin-left:34px}
.site-header .btn{margin-left:26px}
.hero-copy{position:absolute;left:152px;top:232px;width:470px}
.hero-copy h1{color:var(--white);font-size:38px;font-weight:800;line-height:1.15}
.hero-copy p{color:#f7b46a;font-size:16px;line-height:1.45;margin:14px 0 22px;font-weight:600}

/* recipes */
.recipes{position:absolute;left:0;top:592px;width:1200px;height:508px;background:var(--panel)}
.section-title{color:var(--orange);font-size:36px;font-weight:900;text-align:center;letter-spacing:1px}
.recipes .section-title{margin-top:136px}
.recipe-grid{position:absolute;left:152px;top:220px;display:flex;gap:24px}
.recipe-card{width:206px;background:var(--white);box-shadow:0 2px 8px rgba(0,0,0,.08)}
.recipe-photo{height:124px}
.recipe-card h3{color:var(--ink);font-size:14px;font-weight:800;text-align:center;margin-top:14px}
.recipe-card p{font-size:11px;text-align:center;line-height:1.4;padding:4px 18px 18px}
.recipes-more{position:absolute;left:0;top:1086px;width:1200px;text-align:center}

/* blog */
.blog-title{position:absolute;left:152px;top:1134px;color:var(--ink);font-size:40px;font-weight:900}
.post-list{position:absolute;left:152px;top:1212px;width:580px}
.post{display:flex;height:272px}
.post-photo{width:240px;height:240px;flex:none}
.post-body{margin-left:28px;padding-top:4px}
.post-meta{font-size:12px;color:var(--ink);font-weight:700;display:flex;gap:22px}
.post-body h2{color:var(--ink);font-size:19px;font-weight:800;line-height:1.2;margin:12px 0 10px}
.post-body p{font-size:12px;line-height:1.5;margin-bottom:14px}

/* sidebar */
.sidebar{position:absolute;left:760px;top:1140px;width:272px}
.widget{background:var(--panel);margin-bottom:32px}
.widget-title{color:var(--ink);font-size:24px;font-weight:900;text-align:center}
.about{height:380px;padding-top:24px;text-align:center}
.about-avatar{width:110px;height:110px;border-radius:50%;margin:18px auto 14px;background:radial-gradient(circle at 50% 40%,#d9b293,#8a6246)}
.about h4{color:var(--orange);font-size:20px;font-weight:900}
.about p{font-size:12px;line-height:1.45;padding:8px 30px 0}
.more-posts{height:448px;padding:22px 22px 0}
.more-posts .widget-title{text-align:left;margin-bottom:16px}
.mini-post{display:flex;gap:12px;margin-bottom:22px}
.mini-photo{width:70px;height:70px;flex:none}
.mini-post p{font-size:11px;line-height:1.35;color:var(--text)}
.mini-post span{display:block;font-size:10px;color:var(--muted);margin-top:4px}
.signup{height:328px;background:var(--orange);padding:26px 26px 0;text-align:center}
.signup .widget-title{color:var(--white);font-size:26px}
.signup p{color:#ffe0bd;font-size:12px;line-height:1.45;margin:10px 0 16px}
.field{background:var(--white);border-radius:20px;height:34px;text-align:left;padding:9px 16px;font-size:12px;color:var(--muted);margin-bottom:12px}
.signup-btn{display:block;background:var(--ink);color:var(--white);font-weight:800;font-size:13px;border-radius:20px;height:38px;line-height:38px;margin:4px 20px 0}
.promo{position:relative;height:288px;margin-bottom:0}
.promo-photo{position:absolute;inset:0;background:linear-gradient(180deg,#d8cfc3 0%,#b89066 55%,#6e4a2c 100%)}
.promo h3{position:absolute;left:0;right:0;top:36px;text-align:center;color:var(--ink);font-size:26px;font-weight:900;line-height:1.15;letter-spacing:1px}

/* pagination */
.pagination{position:absolute;left:152px;top:3138px;display:flex;gap:8px}
.pagination span{width:28px;height:28px;border:1px solid var(--line);display:flex;align-items:center;justify-content:center;font-size:12px;color:var(--text)}
.pagination .current{background:var(--orange);border-color:var(--orange);color:var(--white)}

/* footer */
.site-footer{position:absolute;left:0;top:3232px;width:1200px;height:376px;background:var(--footer)}
.footer-brand{position:absolute;left:160px;top:100px;font-size:34px}
.footer-col{position:absolute;top:54px}
.footer-col h5{color:var(--white);font-size:20px;font-weight:800;margin-bottom:14px}
.footer-col li{list-style:none;color:#c9c9c9;font-size:12px;line-height:1.75}
.col-sitemap{left:400px}
.col-archives{left:628px}
.col-contact{left:832px;width:220px}
.contact-row{display:flex;gap:12px;margin-bottom:14px;align-items:flex-start}
.contact-icon{width:28px;height:28px;border-radius:50%;background:var(--orange);flex:none;display:flex;align-items:center;justify-content:center}
.contact-row p{color:#c9c9c9;font-size:11px;line-height:1.4}
.footer-bottom{position:absolute;left:0;bottom:0;width:1200px;height:56px;background:var(--footer-deep);border-top:1px solid #444;color:#c9c9c9;font-size:12px;text-align:center;line-height:56px}
</style>
</head>
<body>

<section class="hero">
  <div class="hero-photo" role="img" aria-label="Baker's hands dusting flour over bread dough on a wooden table"></div>
  <div class="hero-shade"></div>
  <header class="site-header">
    <div class="brand">Velmo42.com</div>
    <nav class="main-nav">
      <a>Tutorials</a><a>Bread Making</a><a>Reviews</a><a>Blog</a><a>About</a>
    </nav>
    <svg class="search-icon" width="18" height="18" viewBox="0 0 18 18"><circle cx="7.5" cy="7.5" r="5.5" fill="none" stroke="#fff" stroke-width="2"/><line x1="11.5" y1="11.5" x2="16" y2="16" stroke="#fff" stroke-width="2.2" stroke-linecap="round"/></svg>
    <span class="btn">Recipes</span>
  </header>
  <div class="hero-copy">
    <h1>Sed ut perspiciande volup tatac cusantium</h1>
    <p>At vero eos et accusamus et iusto odio digni ssimos ducimus qui blanditiis</p>
    <span class="btn">Read more</span>
  </div>
</section>

<section class="recipes">
  <h2 class="section-title">RECIPES</h2>
  <div class="recipe-grid">
    <article class="recipe-card">
      <div class="recipe-photo" role="img" aria-label="Baker holding a fresh loaf" style="background:linear-gradient(135deg,#e6dccf,#b98c62)"></div>
      <h3>Recipe Name</h3><p>Sed ut perspiciatis unde omnis iste natusu</p>
    </article>
    <article class="recipe-card">
      <div class="recipe-photo" role="img" aria-label="Bread dough on a floured board" style="background:linear-gradient(135deg,#cbb59a,#7d5a3c)"></div>
      <h3>Recipe Name</h3><p>Sed ut perspiciatis unde omnis iste natusu</p>
    </article>
    <article class="recipe-card">
      <div class="recipe-photo" role="img" aria-label="Sliced artisan loaf" style="background:linear-gradient(135deg,#b38a5e,#5a3b24)"></div>
      <h3>Recipe Name</h3><p>Sed ut perspiciatis unde omnis iste natusu</p>
    </article>
    <article class="recipe-card">
      <div class="recipe-photo" role="img" aria-label="Crusty baguettes and rolls" style="background:linear-gradient(135deg,#8d6a4a,#3a2819)"></div>
      <h3>Recipe Name</h3><p>Sed ut perspiciatis unde omnis iste natusu</p>
    </article>
  </div>
</section>
<div class="recipes-more"><span class="btn">View all recipes</span></div>

<h2 class="blog-title">Latest Blog</h2>
<main class="post-list">
  <article class="post">
    <div class="post-photo" role="img" aria-label="Round dough ball on a floured surface" style="background:linear-gradient(135deg,#c9a27a,#6a4a30)"></div>
    <div class="post-body"><div class="post-meta"><span>October 14, 2020</span><span>5 Comments</span></div>
      <h2>At vero eosetaccusamuset iusto odio dignissimoc</h2>
      <p>At vero eos et accusamusand iusto odio dignissimos ducimus qui blanditiis praesentium voluptatum deleniti atque corr upti quos dolores et quasi</p><span class="btn btn-sm">Read more</span></div>
  </article>
  <article class="post">
    <div class="post-photo" role="img" aria-label="Baker kneading dough in a kitchen" style="background:linear-gradient(135deg,#e2d6c6,#9a7a5a)"></div>
    <div class="post-body"><div class="post-meta"><span>October 14, 2020</span><span>5 Comments</span></div>
      <h2>At vero eosetaccusamuset iusto odio dignissimoc</h2>
      <p>At vero eos et accusamusand iusto odio dignissimos ducimus qui blanditiis praesentium voluptatum deleniti atque corr upti quos dolores et quasi</p><span class="btn btn-sm">Read more</span></div>
  </article>
  <article class="post">
    <div class="post-photo" role="img" aria-label="Bakery counter with bread loaves" style="background:linear-gradient(135deg,#d6cfc6,#7e6a56)"></div>
    <div class="post-body"><div class="post-meta"><span>October 14, 2020</span><span>5 Comments</span></div>
      <h2>At vero eosetaccusamuset iusto odio dignissimoc</h2>
      <p>At vero eos et accusamusand iusto odio dignissimos ducimus qui blanditiis praesentium voluptatum deleniti atque corr upti quos dolores et quasi</p><span class="btn btn-sm">Read more</span></div>
  </article>
  <article class="post">
    <div class="post-photo" role="img" aria-label="Assorted golden bread loaves" style="background:linear-gradient(135deg,#c08850,#4e3018)"></div>
    <div class="post-body"><div class="post-meta"><span>October 14, 2020</span><span>5 Comments</span></div>
      <h2>At vero eosetaccusamuset iusto odio dignissimoc</h2>
      <p>At vero eos et accusamusand iusto odio dignissimos ducimus qui blanditiis praesentium voluptatum deleniti atque corr upti quos dolores et quasi</p><span class="btn btn-sm">Read more</span></div>
  </article>
  <article class="post">
    <div class="post-photo" role="img" aria-label="Flour sprinkled over dough on a dark table" style="background:linear-gradient(135deg,#4a3a30,#1e1814)"></div>
    <div class="post-body"><div class="post-meta"><span>October 14, 2020</span><span>5 Comments</span></div>
      <h2>At vero eosetaccusamuset iusto odio dignissimoc</h2>
      <p>At vero eos et accusamusand iusto odio dignissimos ducimus qui blanditiis praesentium voluptatum deleniti atque corr upti quos dolores et quasi</p><span class="btn btn-sm">Read more</span></div>
  </article>
  <article class="post">
    <div class="post-photo" role="img" aria-label="Hands shaping dough" style="background:linear-gradient(135deg,#d9c2a6,#8a6040)"></div>
    <div class="post-body"><div class="post-meta"><span>October 14, 2020</span><span>5 Comments</span></div>
      <h2>At vero eosetaccusamuset iusto odio dignissimoc</h2>
      <p>At vero eos et accusamusand iusto odio dignissimos ducimus qui blanditiis praesentium voluptatum deleniti atque corr upti quos dolores et quasi</p><span class="btn btn-sm">Read more</span></div>
  </article>
  <article class="post">
    <div class="post-photo" role="img" aria-label="Floured dough being rolled out" style="background:linear-gradient(135deg,#e8e2da,#a59484)"></div>
    <div class="post-body"><div class="post-meta"><span>October 14, 2020</span><span>5 Comments</span></div>
      <h2>At vero eosetaccusamuset iusto odio dignissimoc</h2>
      <p>At vero eos et accusamusand iusto odio dignissimos ducimus qui blanditiis praesentium voluptatum deleniti atque corr upti quos dolores et quasi</p><span class="btn btn-sm">Read more</span></div>
  </article>
</main>

<aside class="sidebar">
  <section class="widget about">
    <h3 class="widget-title">About Us</h3>
    <div class="about-avatar" role="img" aria-label="Portrait of the blog author"></div>
    <h4>Marisol Venn</h4>
    <p>At vero eos et accusamusand iusto odio dignissimos du qui blanditiis praesentium voluptatum deleniti atque corrupti quos dolo exceptur sint occae</p>
  </section>
  <section class="widget more-posts">
    <h3 class="widget-title">See More Posts</h3>
    <div class="mini-post"><div class="mini-photo" role="img" aria-label="Bread loaf" style="background:linear-gradient(135deg,#b8865a,#5a3a22)"></div><p>At vero eos et accusam iusto odio dignissim iusto odio cetuissi<span>October 12, 2020</span></p></div>
    <div class="mini-post"><div class="mini-photo" role="img" aria-label="Dough on a board" style="background:linear-gradient(135deg,#d8c4aa,#8a6a4a)"></div><p>At vero eos et accusam iusto odio dignissim iusto odio cetuissi<span>October 12, 2020</span></p></div>
    <div class="mini-post"><div class="mini-photo" role="img" aria-label="Sliced bread" style="background:linear-gradient(135deg,#a77a50,#4a2f1a)"></div><p>At vero eos et accusam iusto odio dignissim iusto odio cetuissi<span>October 12, 2020</span></p></div>
    <div class="mini-post"><div class="mini-photo" role="img" aria-label="Baguettes" style="background:linear-gradient(135deg,#c99a66,#6a4426)"></div><p>At vero eos et accusam iusto odio dignissim iusto odio cetuissi<span>October 12, 2020</span></p></div>
  </section>
  <section class="widget signup">
    <h3 class="widget-title">Get more stuff</h3>
    <p>At vero eos et accusamus et iusto odio dignissimos ducimus qui blanditiis praesentium</p>
    <div class="field">Name</div>
    <div class="field">Email</div>
    <span class="signup-btn">SIGN UP</span>
  </section>
  <section class="widget promo">
    <div class="promo-photo" role="img" aria-label="Bread loaves on a light backdrop"></div>
    <h3>FINIBUSONO<br>RUM ETMRUM</h3>
  </section>
</aside>

<nav class="pagination">
  <span class="current">1</span><span>2</span><span>3</span><span>4</span><span>5</span><span>6</span>
  <span><svg width="8" height="10" viewBox="0 0 8 10"><path d="M2 1l4 4-4 4" fill="none" stroke="#555" stroke-width="1.6"/></svg></span>
</nav>

<footer class="site-footer">
  <div class="brand footer-brand">Velmo42.com</div>
  <div class="footer-col col-sitemap">
    <h5>Sitemap</h5>
    <ul><li>Sed ut podio</li><li>Bunde omnis iste</li><li>Natus error sites</li><li>Epsilons novusin</li><li>Nihum doleirmqu</li><li>Exsullanbum</li><li>Ritem cet persam</li></ul>
  </div>
  <div class="footer-col col-archives">
    <h5>Archives</h5>
    <ul><li>October 2020</li><li>September 2020</li><li>August 2020</li><li>July 2020</li><li>June 2020</li><li>May 2020</li><li>April 2020</li></ul>
  </div>
  <div class="footer-col col-contact">
    <h5>Contact</h5>
    <div class="contact-row"><span class="contact-icon"><svg width="12" height="14" viewBox="0 0 12 14"><path d="M6 13S1 8 1 5a5 5 0 0 1 10 0c0 3-5 8-5 8z" fill="#fff"/><circle cx="6" cy="5" r="1.8" fill="#f2891c"/></svg></span><p>Sed ut perspiciatis unde omnis iste natus error</p></div>
    <div class="contact-row"><span class="contact-icon"><svg width="12" height="12" viewBox="0 0 12 12"><path d="M2 1h2l1 3-1.5 1a7 7 0 0 0 3.5 3.5L8 7l3 1v2a1 1 0 0 1-1 1A9 9 0 0 1 1 2a1 1 0 0 1 1-1z" fill="#fff"/></svg></span><p>Phone:<br>555 018 4270</p></div>
    <div class="contact-row"><span class="contact-icon"><svg width="13" height="10" viewBox="0 0 13 10"><rect x=".5" y=".5" width="12" height="9" fill="#fff"/><path d="M.5 .5l6 5 6-5" fill="none" stroke="#f2891c" stroke-width="1.2"/></svg></span><p>Email:<br>hello@velmo42.com</p></div>
  </div>
  <div class="footer-bottom">© 2020 All Rights are reserved | Privacy | Terms of use</div>
</footer>

</body>
</html>
```